I need a website built for my modeling agency company.

On our website, a user can create a profile and we will submit it to thousands of modeling agents throughout the country.

In many cases, they will receive multiple offers from modeling agencies which allows them to pick and choose the contract that is best for them to launch their modeling career.

Some tag lines to consider using:

"Submit your profile to hundreds of modeling agents instantly!"

"Get found and become a star!"

We are: The Runway Guild.

Our Slogan: The World''s Largest Network of Fashion Models and Agents

What We Do: We are an agency with one of the largest networks of fashion professionals that are looking for new modeling talent. We host professional profiles for aspiring models, professional fashion models seeking work, modeling talent seekers, and top modeling agencies. We connect aspiring models with the top modeling agencies in the United States and abroad.

By submitting your FREE profile, you will be instantly introduced to the industry’s leading modeling agents. Within a few days, you could receive multiple, competing offers from modeling agencies that all want to launch your modeling career. Receiving multiple signing offers puts you in control of deciding which contract best suites you!

Reason: I've seen some good designs, but none that are 100% perfect. These are the ones that I like best so far (to give you some ideas): http://files.pixelvane.example/img/510372/820114/820114_4917263_510372_image.jpg http://files.pixelvane.example/img/510372/829305/829305_4926851_510372_image.jpg http://files.pixelvane.example/img/510372/51847/51847_4924097_510372_image.jpg http://files.pixelvane.example/img/510372/51847/51847_4919856_510372_image.jpg http://files.pixelvane.example/img/510372/823670/823670_4920438_510372_image.jpg

Target Market(s)

Aspiring models (mostly female, but some male)

Industry/Entity Type

Modeling Agency

Colors

Designer to choose colors to be used in the design.

Requirements
Nice to have
• Somewhere in the top half of the page, I would like there to be a small form for the visitor to fill out. This form will look as follows:

Title: Instantly contact hundreds of modeling agents who are looking for new talent and could make you a star!
Fields: First Name*, Last Name*, Age, Zip Code, Email Address*, Daytime Phone, Evening Phone, Comments.

Then, there will be a "submit" button to proceed to next step of form. Just below the "submit" button, should be the following verbiage: "You will have the opportunity to upload photo(s) and provide other pertinent information in next step."

```html
<!DOCTYPE html>
<html lang="en">
<head>
<meta charset="utf-8">
<title>The Runway Guild</title>
<link href="https://fonts.googleapis.com/css2?family=Figtree:wght@400;500;600;700;800&family=Barlow+Semi+Condensed:wght@500&display=swap" rel="stylesheet">
<style>
:root{
  --pink:#e6168e;
  --pink-dark:#c70f79;
  --black:#111;
  --ink:#222;
  --grey-panel:#e4e4e4;
  --line:#e2e2e2;
  --yellow:#ffe600;
  --page:#f3f3f3;
}
*{box-sizing:border-box;margin:0;padding:0}
html,body{width:1200px;height:960px;overflow:hidden}
body{position:relative;background:#fff;font-family:"Figtree",Arial,sans-serif;color:var(--ink)}
.side-photo{position:absolute;top:39px;width:163px;height:880px}
.side-photo.left{left:0;background:linear-gradient(180deg,#4a3a3c 0%,#7a6a6c 35%,#c9b8bb 65%,#fff 90%)}
.side-photo.right{right:0;background:linear-gradient(180deg,#d8c4c0 0%,#ef8ea0 30%,#f6a9b6 60%,#fde6ea 85%,#fff 100%)}
.topbar{position:absolute;top:0;left:0;width:1200px;height:39px;background:linear-gradient(#ee2a9b,var(--pink))}
.topbar .social{position:absolute;left:657px;top:10px;display:flex;gap:5px}
.topbar .social span{width:18px;height:18px;border-radius:50%;background:#fff}
.account{position:absolute;left:730px;top:7px;width:103px;height:23px;background:#fff;font-size:12px;color:#777;padding:4px 10px}
.search{position:absolute;left:840px;top:7px;width:197px;height:23px;background:#fff;font-size:12px;color:#888;padding:4px 10px}
.search svg,.account svg{position:absolute;right:8px;top:5px}
.site{position:absolute;left:163px;top:39px;width:874px;height:816px;background:var(--page)}
.header{height:84px;background:#fff;position:relative}
.brand{position:absolute;left:13px;top:14px;display:flex;align-items:center;gap:8px}
.brand .mark{width:30px;height:30px;background:var(--pink)}
.brand .name{font-size:27px;font-weight:500;color:var(--black);letter-spacing:1px;line-height:1}
.brand-slogan{position:absolute;left:13px;top:60px;font-size:9px;color:var(--black)}
.pitch{position:absolute;right:16px;top:20px;text-align:center;font-size:18px;line-height:25px;color:var(--black)}
.pitch em{font-style:normal;color:var(--pink)}
.nav{height:35px;background:linear-gradient(#1f1f1f,#000);display:flex;position:relative;font-family:"Barlow Semi Condensed",sans-serif;font-size:14px}
.nav a{color:#fff;text-decoration:none;line-height:35px;padding:0 9.5px}
.nav a.active{background:var(--pink);padding:0 12px 0 14px}
.nav .create{position:absolute;right:0;top:0;width:119px;background:var(--pink);text-align:center}
.slider{position:absolute;left:14px;top:132px;width:577px;height:214px;background:linear-gradient(180deg,#3a3a3a,#8c8c8c 55%,#e6e2dc)}
.slider .arrow{position:absolute;top:96px;width:23px;height:23px;border-radius:50%;background:#fff}
.slider .arrow svg{position:absolute;left:7px;top:7px}
.promo{position:absolute;left:603px;top:132px;width:256px;height:214px;background:linear-gradient(135deg,#d00a7c,#e94aa6 55%,#c6086f);text-align:center;color:#fff;font-weight:800}
.promo .l1{margin-top:48px;font-size:25px;letter-spacing:.5px}
.promo .l2{font-size:23px;margin-top:2px}
.promo .l3{font-size:34px;color:var(--yellow);line-height:1.1}
.promo .btn{display:inline-flex;align-items:center;gap:14px;margin-top:10px;background:#000;color:#fff;font-weight:400;font-size:15px;padding:5px 10px}
h2{position:absolute;font-size:18px;font-weight:400;color:var(--black)}
.cards{position:absolute;left:14px;display:flex;gap:14px}
.agency{width:133px;height:159px;background:#fff;position:relative}
.agency .logo{height:106px;background:linear-gradient(135deg,#555,#2a2a2a);color:#fff;font-size:16px;display:flex;align-items:center;justify-content:center}
.agency .logo::after{content:"";position:absolute;left:9px;top:99px;border:6px solid transparent;border-bottom-color:#fff;border-top:0}
.card-name{color:var(--pink);font-size:12px;padding:10px 10px 3px}
.card-loc{font-size:10px;color:var(--black);padding:0 10px}
.model{width:133px;height:198px;background:#fff;margin-right:14px}
.model:last-child{margin-right:0}
.model .photo{height:175px}
.model .card-name{padding:5px 10px}
.profiles{position:absolute;left:603px;top:385px;width:256px;height:292px;background:#fff;padding:12px 17px 0 17px}
.profile{border-bottom:1px solid var(--line);padding:4px 0 6px 0;font-size:9.5px;line-height:15px;color:var(--black)}
.profile:last-child{border-bottom:0}
.profile b{display:block;font-weight:400;color:var(--pink);font-size:13px;line-height:18px}
.newsletter{position:absolute;left:603px;top:677px;width:256px;height:117px;background:var(--grey-panel);padding:11px 18px}
.newsletter h3{font-size:18px;font-weight:400;color:var(--black)}
.newsletter .field{margin-top:10px;height:29px;background:#fff;border:1px solid #ccc;font-size:9.5px;padding:8px 10px}
.newsletter .go{display:inline-block;margin-top:9px;background:var(--pink);color:#fff;font-size:15px;padding:3px 11px}
.footer-nav{position:absolute;top:877px;left:0;width:1200px;text-align:center;font-family:"Barlow Semi Condensed",sans-serif;font-size:11px;color:var(--black)}
.footer-nav span{margin:0 5px}
.copy{position:absolute;top:898px;width:1200px;text-align:center;font-size:9.5px}
.footer-social{position:absolute;top:919px;left:548px;display:flex;gap:5px}
.footer-social span{width:26px;height:26px;border-radius:50%;background:#000}
</style>
</head>
<body>
<div class="side-photo left" role="img" aria-label="Runway photo of a model walking"></div>
<div class="side-photo right" role="img" aria-label="Model in a pink sequinned gown on the runway"></div>

<div class="topbar">
  <div class="social"><span></span><span></span><span></span></div>
  <div class="account">My Account
    <svg width="11" height="12" viewBox="0 0 11 12"><circle cx="5.5" cy="3.5" r="3" fill="#999"/><path d="M0 12c0-4 11-4 11 0z" fill="#999"/></svg></div>
  <div class="search">Search
    <svg width="13" height="13" viewBox="0 0 13 13"><circle cx="5.5" cy="5.5" r="4.5" fill="none" stroke="#aaa" stroke-width="1.5"/><path d="M9 9l3.5 3.5" stroke="#aaa" stroke-width="1.5"/></svg></div>
</div>

<div class="site">
  <div class="header">
    <div class="brand"><span class="mark"></span><span class="name">The Runway Guild</span></div>
    <div class="brand-slogan">The World's Largest Network of Fashion Models and Agents</div>
    <div class="pitch">Submit your profile to hundreds of<br>modeling agents <em>instantly!</em></div>
  </div>
  <nav class="nav">
    <a class="active">HOME</a><a>ABOUT US</a><a>MODELING AGENCIES</a><a>BECOME A MODEL</a><a>MEN</a><a>WOMAN</a><a>BLOG</a><a>CONTACT US</a>
    <a class="create">CREATE PROFILE ▶</a>
  </nav>

  <div class="slider" role="img" aria-label="Group of models in white and pastel dresses on a runway">
    <span class="arrow" style="left:11px"><svg width="9" height="9" viewBox="0 0 9 9"><path d="M7 0v9L1 4.5z" fill="#000"/></svg></span>
    <span class="arrow" style="right:11px"><svg width="9" height="9" viewBox="0 0 9 9"><path d="M2 0v9l6-4.5z" fill="#000"/></svg></span>
  </div>
  <div class="promo">
    <div class="l1">BECOME A MODEL</div>
    <div class="l2">START YOUR STAR</div>
    <div class="l3">CAREER</div>
    <div class="btn">Click here <svg width="8" height="13" viewBox="0 0 8 13"><path d="M1 1l5.5 5.5L1 12" fill="none" stroke="var(--pink)" stroke-width="2"/></svg></div>
  </div>

  <h2 style="left:14px;top:355px">MODELING AGENCIES</h2>
  <div class="cards" style="top:385px">
    <div class="agency"><div class="logo">LOGO HERE</div><div class="card-name">Lorem Ipsum</div><div class="card-loc">New York, USA</div></div>
    <div class="agency"><div class="logo">LOGO HERE</div><div class="card-name">Lorem Ipsum</div><div class="card-loc">New York, USA</div></div>
    <div class="agency"><div class="logo">LOGO HERE</div><div class="card-name">Lorem Ipsum</div><div class="card-loc">New York, USA</div></div>
    <div class="agency"><div class="logo">LOGO HERE</div><div class="card-name">Lorem Ipsum</div><div class="card-loc">New York, USA</div></div>
  </div>

  <h2 style="left:14px;top:565px">NEWEST ADD MODELS</h2>
  <div class="cards" style="top:596px;gap:0">
    <div class="model"><div class="photo" role="img" aria-label="Portrait of a model in red" style="background:linear-gradient(#6b4a38,#a8322c)"></div><div class="card-name">Lorem Ipsum</div></div>
    <div class="model"><div class="photo" role="img" aria-label="Portrait of a red-haired model" style="background:linear-gradient(#8fa2b0,#c98a6a)"></div><div class="card-name">Lorem Ipsum</div></div>
    <div class="model"><div class="photo" role="img" aria-label="Model in a yellow swimsuit by a tiled pool" style="background:linear-gradient(#4aa7d6,#d8c44a)"></div><div class="card-name">Lorem Ipsum</div></div>
    <div class="model"><div class="photo" role="img" aria-label="Portrait of a model with earrings" style="background:linear-gradient(#3c5a58,#c9a07c)"></div><div class="card-name">Lorem Ipsum</div></div>
  </div>

  <h2 style="left:603px;top:355px">NEWEST MODEL PROFILES</h2>
  <div class="profiles">
    <div class="profile"><b>Liesbeth</b>Location: Spain | Sex: female<br>Jobs: Photo shoot Advertising production</div>
    <div class="profile"><b>Patrick</b>Location: Spain | Sex: female<br>Jobs: Photo shoot Advertising production</div>
    <div class="profile"><b>Carla</b>Location: Spain | Sex: female<br>Jobs: Photo shoot Advertising production</div>
    <div class="profile"><b>Ricky</b>Location: Spain | Sex: female<br>Jobs: Photo shoot Advertising production</div>
    <div class="profile"><b>Ozge</b>Location: Spain | Sex: female</div>
  </div>
  <div class="newsletter">
    <h3>NEWSLETTER SUBSCRIBE</h3>
    <div class="field">E-mail Address</div>
    <div class="go">Subscribe</div>
  </div>
</div>

<div class="footer-nav">HOME<span>|</span>ABOUT US<span>|</span>MODELING AGENCIES<span>|</span>BECOME A MODEL<span>|</span>MEN<span>|</span>WOMAN<span>|</span>BLOG<span>|</span>CONTACT US</div>
<div class="copy">Copyrights 2013 Runway Guild, All Rights Reserved.</div>
<div class="footer-social"><span></span><span></span><span></span></div>
</body>
</html>
```